Icon-Design für Entwicklung von IT-Anwendungen
Zielgruppe
Entwicklung von IT-Anwendungen - Schwerpunkt sind Intranet-Anwendungen
Aufgabenstellung
Modernes Button-Layout mit Fokus auf 'technisches', eher schnörkelloses Design
1. Gewünscht wird ein modernes Layout für 8 Buttons (vgl. alte Buttons in buttons.png). Für jede Aktion (z.B. Einzelprojekt bearbeiten, Speichern, Löschen, usw.) soll ein aussagefähiges Icon und der jeweilige Text enthalten sein.
2. Für jeden Button soll es eine Highlight-Variante geben (für spätere MouseOver-Anwendung)
3. Weiterhin wird eine Leiste gewünscht, in die die Buttons später integriert werden. Als Farbe soll ein Blauton verwendet werden, der zum restlichen Blau harmoniert.
Technische Vorgaben für Buttons
- Größe jeweils 130 x 34 Pixel
- Hintergrundfarbe transparent
- Photoshop-Dateiformat, so dass Texte editierbar bleiben
Technische Vorgaben für Leiste
- Größe 1320 x 40 Pixel
- PNG-Dateiformat

```html
<!DOCTYPE html>
<html lang="de">
<head>
<meta charset="utf-8">
<title>Button-Leiste mit Rollover-Effekten</title>
<link rel="stylesheet" href="https://fonts.googleapis.com/css2?family=Source+Sans+3:wght@400;700&display=swap">
<style>
  :root {
    --canvas: #ffffff;
    --bar-top: #ececec;
    --bar-mid: #f6f6f6;
    --bar-bottom: #e2e2e2;
    --btn-top: #f7f7f7;
    --btn-bottom: #cfcfcf;
    --btn-ring: #e9e9e9;
    --icon: #555555;
    --label: #4a4a4a;
    --title: #a5a5a5;
    --danger-top: #e8332f;
    --danger-bottom: #c8100e;
    --primary-top: #3a8be6;
    --primary-bottom: #1d68cf;
    --light: #ffffff;
    --cursor-line: #111111;
  }
  * { box-sizing: border-box; margin: 0; padding: 0; }
  html, body { width: 1200px; height: 416px; overflow: hidden; background: var(--canvas); }
  body { position: relative; font-family: "Source Sans 3", sans-serif; }

  .toolbar {
    position: absolute; left: 90px; width: 1020px; height: 31px;
    background: linear-gradient(to bottom, var(--bar-top), var(--bar-mid) 50%, var(--bar-bottom));
  }
  .toolbar--default { top: 75px; }
  .toolbar--danger  { top: 248px; }
  .toolbar--primary { top: 313px; }

  .action {
    position: absolute; top: 3px; width: 93px; height: 25px;
    border-radius: 13px;
    background: linear-gradient(to bottom, var(--btn-top), var(--btn-bottom));
    box-shadow: 0 0 0 2px var(--btn-ring), 0 1.5px 1.5px rgba(0,0,0,.25);
    display: flex; align-items: center;
    color: var(--label);
  }
  .action:nth-child(1) { left: 12px; }
  .action:nth-child(2) { left: 141px; }
  .action:nth-child(3) { left: 270px; }
  .action:nth-child(4) { left: 399px; }
  .action:nth-child(5) { left: 528px; }
  .action:nth-child(6) { left: 657px; }
  .action:nth-child(7) { left: 786px; }
  .action:nth-child(8) { left: 915px; }

  .action__icon { width: 24px; height: 17px; margin-left: 8px; flex: none; fill: var(--icon); }
  .action__label { margin-left: 7px; font-size: 7.2px; line-height: 8.4px; white-space: nowrap; }

  .action--danger { background: linear-gradient(to bottom, var(--danger-top), var(--danger-bottom)); }
  .action--primary { background: linear-gradient(to bottom, var(--primary-top), var(--primary-bottom)); }
  .action--danger, .action--primary { color: var(--light); }
  .action--danger .action__icon, .action--primary .action__icon { fill: var(--light); }
  .action--danger .action__label, .action--primary .action__label { font-weight: 700; }

  .section-title {
    position: absolute; left: 95px; top: 205px;
    font-size: 21px; font-weight: 700; color: var(--title); letter-spacing: .2px;
  }

  .pointer { position: absolute; width: 24px; height: 30px; }
  .pointer--danger { left: 1086px; top: 265px; }
  .pointer--primary { left: 305px; top: 332px; }
</style>
</head>
<body>
<svg width="0" height="0" style="position:absolute">
  <defs>
    <symbol id="i-folder-plus" viewBox="0 0 24 17"><path d="M1 3h6l2 2h8v11H1z"/><path d="M16 3h3V0h2v3h3v2h-3v3h-2V5h-3z"/></symbol>
    <symbol id="i-doc-search" viewBox="0 0 24 17"><path d="M5 2h7v4a6 6 0 0 0 3 8v3H5z"/><circle cx="16" cy="7" r="4.5" fill="none" stroke="currentColor" stroke-width="2" style="stroke:inherit"/><path d="M16 2.5a4.5 4.5 0 1 1 0 9a4.5 4.5 0 0 1 0-9zm0 1.8a2.7 2.7 0 1 0 0 5.4a2.7 2.7 0 0 0 0-5.4z"/><path d="M18.5 10.5l1.4-1.4 3.6 3.6-1.4 1.4z"/></symbol>
    <symbol id="i-folder-search" viewBox="0 0 24 17"><path d="M0 3h6l2 2h5a6 6 0 0 0 2 11H2z"/><path d="M17 3a5 5 0 1 1 0 10a5 5 0 0 1 0-10zm0 2a3 3 0 1 0 0 6a3 3 0 0 0 0-6z"/><path d="M20 12l1.4-1.4 2.6 2.6-1.4 1.4z"/></symbol>
    <symbol id="i-edit" viewBox="0 0 24 17"><path d="M6 5l6-5 7 8-6 5z"/><path d="M3 10l3-3 6 7-3 3z"/><path d="M9 4l1-1 5 6-1 1z" fill="#fff" opacity=".5"/></symbol>
    <symbol id="i-save-back" viewBox="0 0 24 17"><path d="M2 0h13l3 3v6h-3a5 5 0 0 0-4 8H2z"/><path d="M5 0h7v5H5z" fill="#fff" opacity=".6"/><path d="M15 10l-3 3 3 3v-2h2a2 2 0 0 1 2 2h2a4 4 0 0 0-4-4h-2z"/></symbol>
    <symbol id="i-save-next" viewBox="0 0 24 17"><path d="M2 0h13l3 3v6h-3a5 5 0 0 0-4 8H2z"/><path d="M5 0h7v5H5z" fill="#fff" opacity=".6"/><path d="M19 10l3 3-3 3v-2h-2a2 2 0 0 0-2 2h-2a4 4 0 0 1 4-4h2z"/></symbol>
    <symbol id="i-duplicate" viewBox="0 0 24 17"><path d="M2 2h6l2 2h10v2H4z"/><path d="M0 6h24l-2 10H2z"/><path d="M3 4h20v1H3z" opacity=".6"/></symbol>
    <symbol id="i-trash" viewBox="0 0 24 17"><path d="M3 2h6V0h4v2h6v2H3z"/><path d="M5 5h12l-1 12H6zm3 2v8h1.5V7zm4.5 0v8H14V7z"/></symbol>
    <symbol id="i-pointer" viewBox="0 0 24 30"><path d="M2 2v22l6-5 4 9 4-2-4-9h8z" fill="#fff" stroke="#111" stroke-width="2.4" stroke-linejoin="round"/></symbol>
  </defs>
</svg>

<div class="toolbar toolbar--default">
  <div class="action"><svg class="action__icon"><use href="#i-folder-plus"/></svg><span class="action__label">Neues Projekt<br>anlegen</span></div>
  <div class="action"><svg class="action__icon"><use href="#i-doc-search"/></svg><span class="action__label">Einzelprojekt-<br>ansicht</span></div>
  <div class="action"><svg class="action__icon"><use href="#i-folder-search"/></svg><span class="action__label">Multiprojekt-<br>ansicht</span></div>
  <div class="action"><svg class="action__icon"><use href="#i-edit"/></svg><span class="action__label">Einzelprojekt<br>bearbeiten</span></div>
  <div class="action"><svg class="action__icon"><use href="#i-save-back"/></svg><span class="action__label">Speichern und zum<br>letzten Projekt</span></div>
  <div class="action"><svg class="action__icon"><use href="#i-save-next"/></svg><span class="action__label">Speichern und zum<br>nächsten Projekt</span></div>
  <div class="action"><svg class="action__icon"><use href="#i-duplicate"/></svg><span class="action__label">Dupliziere<br>dieses Projekt</span></div>
  <div class="action"><svg class="action__icon"><use href="#i-trash"/></svg><span class="action__label">Lösche<br>dieses Projekt</span></div>
</div>

<h2 class="section-title">Rollover-Effekte:</h2>

<div class="toolbar toolbar--danger">
  <div class="action"><svg class="action__icon"><use href="#i-folder-plus"/></svg><span class="action__label">Neues Projekt<br>anlegen</span></div>
  <div class="action"><svg class="action__icon"><use href="#i-doc-search"/></svg><span class="action__label">Einzelprojekt-<br>ansicht</span></div>
  <div class="action"><svg class="action__icon"><use href="#i-folder-search"/></svg><span class="action__label">Multiprojekt-<br>ansicht</span></div>
  <div class="action"><svg class="action__icon"><use href="#i-edit"/></svg><span class="action__label">Einzelprojekt<br>bearbeiten</span></div>
  <div class="action"><svg class="action__icon"><use href="#i-save-back"/></svg><span class="action__label">Speichern und zum<br>letzten Projekt</span></div>
  <div class="action"><svg class="action__icon"><use href="#i-save-next"/></svg><span class="action__label">Speichern und zum<br>nächsten Projekt</span></div>
  <div class="action"><svg class="action__icon"><use href="#i-duplicate"/></svg><span class="action__label">Dupliziere<br>dieses Projekt</span></div>
  <div class="action action--danger"><svg class="action__icon"><use href="#i-trash"/></svg><span class="action__label">Lösche<br>dieses Projekt</span></div>
</div>
<svg class="pointer pointer--danger"><use href="#i-pointer"/></svg>

<div class="toolbar toolbar--primary">
  <div class="action"><svg class="action__icon"><use href="#i-folder-plus"/></svg><span class="action__label">Neues Projekt<br>anlegen</span></div>
  <div class="action action--primary"><svg class="action__icon"><use href="#i-doc-search"/></svg><span class="action__label">Einzelprojekt-<br>ansicht</span></div>
  <div class="action"><svg class="action__icon"><use href="#i-folder-search"/></svg><span class="action__label">Multiprojekt-<br>ansicht</span></div>
  <div class="action"><svg class="action__icon"><use href="#i-edit"/></svg><span class="action__label">Einzelprojekt<br>bearbeiten</span></div>
  <div class="action"><svg class="action__icon"><use href="#i-save-back"/></svg><span class="action__label">Speichern und zum<br>letzten Projekt</span></div>
  <div class="action"><svg class="action__icon"><use href="#i-save-next"/></svg><span class="action__label">Speichern und zum<br>nächsten Projekt</span></div>
  <div class="action"><svg class="action__icon"><use href="#i-duplicate"/></svg><span class="action__label">Dupliziere<br>dieses Projekt</span></div>
  <div class="action"><svg class="action__icon"><use href="#i-trash"/></svg><span class="action__label">Lösche<br>dieses Projekt</span></div>
</div>
<svg class="pointer pointer--primary"><use href="#i-pointer"/></svg>
</body>
</html>
```